brightpathPRESS is publishing a new book and needs some exceptional cover and layout design!

We are publishing a narrow niche PDF eBook and need both a great cover AND great magazine style layout.

The eBook is a compilation of interviews with 12 financial experts on a particular topic. So the format is is the same for each interview 'chapter'

We are looking for a good front cover/document design that will make what is a pretty dry topic, exciting, interesting and easy to read. Basically - magazine style layout.

The specs for the front cover are:

Title:

The Hurdles and Openings Before Bookkeepers and Planners In Expanding Their Pension Practice In 2014 -2015

by Tom Pelliwick

published by brightpathPRESS

The client would like a similar cover to the one I have attached for your reference. (book front cover example). By no means be limited by this design suggestion. The only caveat is that shots of all interview subjects are included (except the author). These have been included in the zip file.

The design for the text should be elegant and consistent with the design of the front cover. Please format the text in pages 1 to 15 to demonstrate you've understood the brief.

Attached files.

1) MS word version of draft book pages 1 to 15
2) copy of the cover my client would like to emulate.

reminder - this is destined to be a PDF eBook - so looking for some nice eye catching magazine style layout in the design. Columns would be fine.

Good luck!

Brent Malloy
brightpathPRESS

Target Market(s)

Professional Accountants who are running there own businesses

Industry/Entity Type

Financial

Colors

Designer to choose colors to be used in the design.

Requirements
Must have
• The cover must feature headshots of all the interview subjects. The PDF layout must be optimised for viewing on an iPad

```html
<!DOCTYPE html>
<html lang="en">
<head>
<meta charset="utf-8">
<title>The Hurdles and Openings Before Bookkeepers and Planners – Cover</title>
<link rel="stylesheet" href="https://fonts.googleapis.com/css2?family=Noto+Sans:wght@400&display=swap">
<style>
  :root {
    --paper: #ffffff;
    --ink: #555555;
    --ink-soft: #444444;
    --sand: #e0dbd2;
    --frame: #9a9a9a;
    --photo-a: #7d7a76;
    --photo-b: #a8a29a;
    --photo-c: #c9c3ba;
    --photo-d: #5f646b;
  }
  * { margin: 0; padding: 0; box-sizing: border-box; }
  html, body {
    width: 840px; height: 1200px; overflow: hidden;
    background: var(--paper);
  }
  .cover {
    position: relative;
    width: 840px; height: 1200px;
    overflow: hidden;
    background: var(--paper);
    font-family: "Noto Sans", "Open Sans", sans-serif;
    color: var(--ink);
  }
  .cover-shapes {
    position: absolute; inset: 0;
    width: 840px; height: 1200px;
  }
  .cover-title {
    position: absolute;
    left: 66px; top: 68px;
    font-weight: 400;
    font-size: 54px;
    line-height: 70px;
    letter-spacing: 1px;
    text-transform: uppercase;
    color: var(--ink);
  }
  .cover-title span { display: block; white-space: nowrap; }
  .experts {
    position: absolute;
    left: 0; width: 840px;
    display: flex;
  }
  .experts.row-one { top: 722px; height: 111px; }
  .experts.row-two { top: 856px; height: 110px; }
  .headshot { flex: 1; height: 100%; }
  .tone-a { background: linear-gradient(180deg, var(--photo-a), var(--photo-d)); }
  .tone-b { background: linear-gradient(180deg, var(--photo-c), var(--photo-b)); }
  .tone-c { background: linear-gradient(180deg, #eeeeee, var(--photo-b)); }
  .tone-d { background: linear-gradient(180deg, #b9c4b0, #6d735f); }
  .publisher {
    position: absolute;
    left: 66px; top: 1064px;
    width: 216px; height: 84px;
    border: 1.5px solid var(--frame);
    padding: 14px 0 0 22px;
    font-size: 18px;
    line-height: 27px;
    color: var(--ink-soft);
  }
  .publisher .label { text-transform: uppercase; letter-spacing: 0.5px; }
  .byline {
    position: absolute;
    left: 444px; top: 1076px;
    display: flex; align-items: baseline;
    white-space: nowrap;
  }
  .byline .by { font-size: 31px; color: var(--ink-soft); margin-right: 30px; }
  .byline .author {
    font-size: 38px; letter-spacing: 1px;
    text-transform: uppercase; color: var(--ink);
  }
</style>
</head>
<body>
  <main class="cover">
    <svg class="cover-shapes" viewBox="0 0 840 1200" aria-hidden="true">
      <path class="arch" fill="var(--sand)"
            d="M528 664 C548 500 610 342 720 342 C790 342 828 380 840 420 L840 664 Z"/>
      <path class="footer-panel" fill="var(--sand)"
            d="M498 1200 L498 1062 C498 1040 510 1026 532 1026 L840 1026 L840 1200 Z"/>
    </svg>

    <h1 class="cover-title">
      <span>The Hurdles</span>
      <span>and Openings Before</span>
      <span>Bookkeepers</span>
      <span>and Planners In</span>
      <span>Expanding Their</span>
      <span>Pension Practice</span>
      <span>In 2014 -2015</span>
    </h1>

    <div class="experts row-one">
      <div class="headshot tone-a" role="img" aria-label="Headshot of interview expert 1"></div>
      <div class="headshot tone-b" role="img" aria-label="Headshot of interview expert 2"></div>
      <div class="headshot tone-c" role="img" aria-label="Headshot of interview expert 3"></div>
      <div class="headshot tone-b" role="img" aria-label="Headshot of interview expert 4"></div>
      <div class="headshot tone-a" role="img" aria-label="Headshot of interview expert 5"></div>
      <div class="headshot tone-c" role="img" aria-label="Headshot of interview expert 6"></div>
      <div class="headshot tone-d" role="img" aria-label="Headshot of interview expert 7"></div>
      <div class="headshot tone-b" role="img" aria-label="Headshot of interview expert 8"></div>
    </div>

    <div class="experts row-two">
      <div class="headshot tone-c" role="img" aria-label="Headshot of interview expert 9"></div>
      <div class="headshot tone-c" role="img" aria-label="Headshot of interview expert 10"></div>
      <div class="headshot tone-d" role="img" aria-label="Headshot of interview expert 11"></div>
      <div class="headshot tone-b" role="img" aria-label="Headshot of interview expert 12"></div>
      <div class="headshot tone-c" role="img" aria-label="Headshot of interview expert 13"></div>
      <div class="headshot tone-c" role="img" aria-label="Headshot of interview expert 14"></div>
      <div class="headshot tone-a" role="img" aria-label="Headshot of interview expert 15"></div>
      <div class="headshot tone-d" role="img" aria-label="Headshot of interview expert 16"></div>
    </div>

    <div class="publisher">
      <div class="label">Published by</div>
      <div class="name">brightpathPRESS</div>
    </div>

    <p class="byline">
      <span class="by">BY</span>
      <span class="author">Tom Pelliwick</span>
    </p>
  </main>
</body>
</html>
```